Biz card, stationary for geriatric clinic
ValdoNorte Residence & Geriatric SPA
Biz card, stationary for geriatric clinic - Health
Creative Brief
Professional
Dra. Tereza Lopes Amaral
Diretora
Dois Irmaos - RS
tereza@valdonorte.example
www.valdonorte.example
We will need stationary i.e. letterhead, envelope, etc. For all business cards we need editable files to change for multiple employees.
Mailing address: Rua Oitenta e sete, 418. CEP 41270-000 | Bairro Jardim Dois Irmaos - RS

```html
<!DOCTYPE html>
<html lang="pt">
<head>
<meta charset="utf-8">
<title>ValdoNorte Residence &amp; Geriatric SPA – Business Card</title>
<link href="https://fonts.googleapis.com/css2?family=Open+Sans:wght@400;600&display=swap" rel="stylesheet">
<style>
  :root {
    --bg: #1f1f21;
    --gold-dark: #8a6a12;
    --gold: #b8922a;
    --gold-light: #dcc06a;
    --cream: #f4f1e4;
    --cream-shade: #e7e2cf;
    --ink: #3a3a32;
    --muted: #8d876f;
  }
  * { margin: 0; padding: 0; box-sizing: border-box; }
  html, body { width: 1200px; height: 874px; overflow: hidden; }
  body {
    background: var(--bg);
    font-family: "Open Sans", Arial, sans-serif;
    position: relative;
  }
  .card {
    position: absolute;
    top: 282px;
    width: 540px;
    height: 310px;
    border-radius: 16px;
    overflow: hidden;
    background: var(--cream);
    box-shadow: 0 10px 30px rgba(0,0,0,.5);
  }
  .card--front { left: 30px; }
  .card--back { left: 630px; }

  .gold-band {
    position: absolute; left: 0; right: 0;
    background: linear-gradient(180deg, var(--gold-light), var(--gold) 45%, var(--gold-dark));
    z-index: 2;
  }
  .card--front .gold-band--top { top: 0; height: 92px; }
  .card--front .gold-band--bottom { bottom: 0; height: 92px; }
  .card--front .cream-band {
    position: absolute; top: 92px; left: 0; right: 0; height: 126px;
    background: linear-gradient(180deg, var(--cream), var(--cream-shade));
  }

  .brand { position: absolute; display: flex; align-items: center; z-index: 3; }
  .brand__mark {
    border-radius: 50%;
    background: radial-gradient(circle at 40% 35%, var(--gold-light), var(--gold) 60%, var(--gold-dark));
    flex: none;
  }
  .brand__name { color: var(--gold); font-weight: 600; line-height: 1.05; }
  .brand__title { display: block; }
  .brand__sub { display: block; }

  .card--front .brand { left: 36px; top: 92px; height: 126px; }
  .card--front .brand__mark { width: 120px; height: 120px; margin-right: 22px; }
  .card--front .brand__title { font-size: 40px; }
  .card--front .brand__sub { font-size: 15px; margin-top: 4px; }
  .card--front .web { font-size: 12px; color: var(--ink); margin-top: 8px; display: block; font-weight: 600; }

  .card--back .gold-band--top { top: 0; height: 78px; }
  .card--back .watermark {
    position: absolute; right: 40px; top: 60px;
    width: 190px; height: 190px; border-radius: 50%;
    background: var(--cream-shade); opacity: .7;
    z-index: 1;
  }
  .person {
    position: absolute; right: 56px; top: 96px; text-align: right;
    z-index: 3;
  }
  .person__name { font-size: 16px; color: #b3ad94; font-weight: 600; }
  .person__role { font-size: 11px; color: #a8a288; margin-top: 4px; }

  .card--back .brand { left: 26px; top: 112px; }
  .card--back .brand__mark { width: 64px; height: 64px; margin-right: 12px; }
  .card--back .brand__title { font-size: 30px; }
  .card--back .brand__sub { font-size: 12px; margin-top: 3px; }

  .contact {
    position: absolute; left: 30px; bottom: 22px;
    font-size: 11.5px; color: var(--ink); line-height: 1.55; list-style: none;
    z-index: 3;
  }
  .contact li { display: flex; align-items: center; gap: 6px; }
  .contact svg { width: 11px; height: 11px; fill: var(--ink); flex: none; }

  .web-vertical {
    position: absolute; right: 12px; top: 140px;
    writing-mode: vertical-rl;
    transform: rotate(180deg);
    font-size: 10px; color: var(--muted); white-space: nowrap;
    z-index: 3;
  }
</style>
</head>
<body>

<section class="card card--front" aria-label="Frente do cartão">
  <div class="gold-band gold-band--top"></div>
  <div class="cream-band"></div>
  <div class="gold-band gold-band--bottom"></div>
  <div class="brand">
    <span class="brand__mark"></span>
    <div class="brand__name">
      <span class="brand__title">ValdoNorte</span>
      <span class="brand__sub">Residence &amp; Geriatric SPA</span>
      <span class="web">www.valdonorte.example</span>
    </div>
  </div>
</section>

<section class="card card--back" aria-label="Verso do cartão">
  <div class="gold-band gold-band--top"></div>
  <span class="watermark" role="img" aria-label="Faint brand emblem area"></span>
  <div class="person">
    <p class="person__name">Dra. Tereza Lopes Amaral</p>
    <p class="person__role">Diretora</p>
  </div>
  <div class="brand">
    <span class="brand__mark"></span>
    <div class="brand__name">
      <span class="brand__title">ValdoNorte</span>
      <span class="brand__sub">Residence &amp; Geriatric SPA</span>
    </div>
  </div>
  <ul class="contact">
    <li>Dois Irmaos - RS</li>
    <li><svg viewBox="0 0 24 24"><path d="M6.6 10.8a15.1 15.1 0 0 0 6.6 6.6l2.2-2.2c.3-.3.7-.4 1-.2 1.1.4 2.3.6 3.6.6.6 0 1 .4 1 1V20c0 .6-.4 1-1 1A17 17 0 0 1 3 4c0-.6.4-1 1-1h3.5c.6 0 1 .4 1 1 0 1.3.2 2.5.6 3.6.1.3 0 .7-.2 1z"/></svg>(051) 3000-4128</li>
    <li><svg viewBox="0 0 24 24"><rect x="6" y="1" width="12" height="22" rx="2"/></svg>(051) 9000-7316</li>
    <li><svg viewBox="0 0 24 24"><path d="M2 5h20v14H2z M2 5l10 8 10-8" stroke="#f4f1e4" stroke-width="1.5"/></svg>tereza@valdonorte.example</li>
  </ul>
  <p class="web-vertical">www.valdonorte.example</p>
</section>

</body>
</html>
```